Dravetti Business Cards

We need a business card design for Dravetti Mining.

This is a B2B company that buys and sells large machinery tires within the coal mining industry. The design should the strong, crisp and masculine. I have uploaded the company logo and rough mock-up of what the back of the card should look like. the front of the card should have the same look/feel as the back. I need editable templates for both the front and the back of the card.

Color scheme should be grey/green/black

Contact information to include on the card:
Name: Owen Pellsworth
Title: Managing Director
Phone: 972-555-0143
Address: 3157 Brantley #5 Dallas, TX 75209
Email: Owen@Dravetti-example.com

I am also opening a contest for letterhead design. If you submit a business card design, please also submit a letterhead design with the same look/feel. The winner of the business card design will also will the letter head and be paid for both.

Target Market(s)

Procurement men/women in the coal mining industry

Industry/Entity Type

Coal Mining

```html
<!DOCTYPE html>
<html lang="en">
<head>
<meta charset="UTF-8">
<title>Dravetti Mining – Business Cards</title>
<link href="https://fonts.googleapis.com/css2?family=Oxanium:wght@700&family=Arimo:wght@400&display=swap" rel="stylesheet">
<style>
  :root {
    --page-bg: #ffffff;
    --card-white: #ffffff;
    --card-edge: #d6d6d6;
    --brand-grey: #5e5f61;
    --body-grey: #6b6b6b;
    --brand-green: #6bb944;
    --back-dark: #141414;
    --back-mid: #303030;
    --back-mark: #0c0c0c;
  }
  * { margin: 0; padding: 0; box-sizing: border-box; }
  html, body {
    width: 1200px;
    height: 1000px;
    overflow: hidden;
    background: var(--page-bg);
  }
  .canvas {
    position: relative;
    width: 1200px;
    height: 1000px;
  }
  .card {
    position: absolute;
    width: 673px;
    height: 385px;
  }
  .card-front {
    left: 281px;
    top: 96px;
    background: var(--card-white);
    border: 2px solid var(--card-edge);
  }
  .brand-lockup {
    position: absolute;
    left: 50px;
    top: 54px;
    display: flex;
    align-items: center;
    gap: 22px;
  }
  .brand-square {
    width: 64px;
    height: 64px;
    background: var(--brand-green);
  }
  .brand-name {
    font-family: "Oxanium", sans-serif;
    font-weight: 700;
    font-size: 62px;
    line-height: 1;
    letter-spacing: 1px;
    color: var(--brand-grey);
    text-transform: uppercase;
  }
  .accent-bar {
    position: absolute;
    left: -2px;
    top: 203px;
    width: 34px;
    height: 122px;
    background: var(--brand-green);
  }
  .contact-block {
    position: absolute;
    left: 50px;
    top: 202px;
  }
  .person-name,
  .person-title {
    font-family: "Oxanium", sans-serif;
    font-weight: 700;
    font-size: 20px;
    line-height: 27px;
    letter-spacing: 0.6px;
    color: var(--brand-grey);
    text-transform: uppercase;
  }
  .contact-lines {
    margin-top: 8px;
    list-style: none;
  }
  .contact-lines li {
    font-family: "Arimo", sans-serif;
    font-size: 17px;
    line-height: 24px;
    color: var(--body-grey);
  }
  .card-back {
    left: 279px;
    top: 525px;
    border: 2px solid var(--card-edge);
    background:
      radial-gradient(ellipse 55% 70% at 50% 40%, var(--back-mid) 0%, var(--back-dark) 75%),
      var(--back-dark);
  }
  .back-mark {
    position: absolute;
    left: 0;
    right: 0;
    top: 40px;
    display: flex;
    flex-direction: column;
    align-items: center;
    gap: 26px;
  }
  .back-square {
    width: 220px;
    height: 220px;
    background: var(--back-mark);
    box-shadow: inset 0 1px 0 rgba(255,255,255,0.05);
  }
  .back-name {
    font-family: "Oxanium", sans-serif;
    font-weight: 700;
    font-size: 40px;
    line-height: 1;
    letter-spacing: 1px;
    color: var(--back-mark);
    text-transform: uppercase;
  }
</style>
</head>
<body>
<main class="canvas">
  <section class="card card-front" aria-label="Business card front">
    <div class="brand-lockup">
      <div class="brand-square"></div>
      <div class="brand-name">Dravetti Mining</div>
    </div>
    <div class="accent-bar"></div>
    <div class="contact-block">
      <p class="person-name">Owen Pellsworth</p>
      <p class="person-title">Managing Director</p>
      <ul class="contact-lines">
        <li>972-555-0143</li>
        <li>3157 Brantley #5 Dallas, TX 75209</li>
        <li>Owen@Dravetti-example.com</li>
      </ul>
    </div>
  </section>

  <section class="card card-back" aria-label="Business card back">
    <div class="back-mark">
      <div class="back-square"></div>
      <div class="back-name">Dravetti Mining</div>
    </div>
  </section>
</main>
</body>
</html>
```